Marlow Estate Services (Handyman / Home Improvement Company)

Looking for a double sided professional looking business card with Logo attached to be highlighted on one side and throwing in an image of a handyman as an option would be nice to see as well. We are a company focused on providing quality Handyman and Home improvement services in a timely manner that is done right the first time with integrity

Industry/Entity Type

Handyman / Home Improvement

Contact Information for Business Card

(LOGO, Name, Mobile and office phone numbers, email) on front side of card, (the words "The SOLUTION to all of your Handyman and Home Improvement needs" followed by "Family Owned and Operated" at the very bottom) on the back.

Colors
EB3D1F
EC4F4E
F09395
F8D3D4
FCEDEE

Requirements
Must have
• Red, Gray, Black Color scheme
Should not have
• No Yellow or Blue colors

```html
<!DOCTYPE html>
<html lang="en">
<head>
<meta charset="utf-8">
<title>Marlow Estate Services – Business Card</title>
<link href="https://fonts.googleapis.com/css2?family=Lato:wght@400;700;900&display=swap" rel="stylesheet">
<style>
  :root {
    --stage: #3a3d40;
    --card-dark: #1c1c1d;
    --card-light: #ffffff;
    --red: #e3141f;
    --ink: #111111;
    --text-gray: #3b3b3b;
    --white: #ffffff;
    --rule: #2a2a2a;
  }
  * { box-sizing: border-box; margin: 0; padding: 0; }
  html, body {
    width: 1200px; height: 1122px; overflow: hidden;
    background: var(--stage);
    font-family: "Lato", sans-serif;
  }
  .card {
    position: absolute;
    width: 720px; height: 411px;
    border-radius: 22px;
    box-shadow: 0 14px 30px rgba(0,0,0,.35);
  }
  /* Back side */
  .card--back {
    left: 80px; top: 80px;
    background: var(--card-dark);
    display: flex; flex-direction: column; align-items: center; justify-content: center;
    text-align: center;
  }
  .brand { display: flex; flex-direction: column; align-items: center; gap: 14px; }
  .brand__dot {
    width: 84px; height: 84px; border-radius: 50%;
    background: var(--red);
  }
  .brand__name {
    font-weight: 900; font-size: 34px; letter-spacing: 1.5px;
    text-transform: uppercase; line-height: 1.1;
  }
  .card--back .brand__name { color: var(--white); }
  .tagline {
    margin-top: 30px;
    font-weight: 900; font-size: 22px; line-height: 1.25;
    color: var(--white); text-transform: uppercase; letter-spacing: .5px;
  }
  .tagline__accent { color: var(--red); }
  .family-note {
    margin-top: 8px;
    font-size: 18px; color: var(--red); font-weight: 400;
  }
  /* Front side */
  .card--front {
    left: 400px; top: 630px;
    background: var(--card-light);
    display: flex; align-items: center;
    padding: 0 40px 0 50px;
  }
  .card--front .brand { width: 300px; }
  .card--front .brand__dot { width: 74px; height: 74px; }
  .card--front .brand__name { color: var(--red); font-size: 28px; text-align: center; }
  .divider {
    width: 1px; height: 200px; background: var(--rule);
    margin: 0 34px 0 20px;
  }
  .contact__name {
    font-weight: 900; font-size: 34px; color: var(--ink);
    text-transform: uppercase; letter-spacing: .5px;
  }
  .contact__role { font-size: 19px; color: var(--red); margin-top: 2px; }
  .contact__list { list-style: none; margin-top: 16px; }
  .contact__item {
    display: flex; align-items: center; gap: 14px;
    font-size: 17px; color: var(--text-gray); line-height: 1.7;
  }
  .contact__icon { width: 16px; height: 16px; flex: none; fill: var(--red); }
</style>
</head>
<body>

<section class="card card--back">
  <div class="brand">
    <div class="brand__dot"></div>
    <div class="brand__name">Marlow Estate Services</div>
  </div>
  <p class="tagline">Your <span class="tagline__accent">Solution</span> to all of your<br>handyman &amp; home improvement needs</p>
  <p class="family-note">Family Owned &amp; Operated</p>
</section>

<section class="card card--front">
  <div class="brand">
    <div class="brand__dot"></div>
    <div class="brand__name">Marlow Estate Services</div>
  </div>
  <div class="divider"></div>
  <div class="contact">
    <h1 class="contact__name">Daniel Reyes</h1>
    <p class="contact__role">Founder &amp; CEO</p>
    <ul class="contact__list">
      <li class="contact__item">
        <svg class="contact__icon" viewBox="0 0 16 16"><path d="M3.5 1l2.5 3-1.5 1.6c.8 2 2.4 3.6 4.4 4.4L10.5 8.5l3 2.5-1.6 2.8C7 13.5 2.5 9 2.2 4.1z"/></svg>
        (123) 456-7890
      </li>
      <li class="contact__item">
        <svg class="contact__icon" viewBox="0 0 16 16"><path d="M4 1h8a1 1 0 011 1v12a1 1 0 01-1 1H4a1 1 0 01-1-1V2a1 1 0 011-1zm1 2v9h6V3zm3 10a.8.8 0 100 .1z"/></svg>
        (123) 456-7890
      </li>
      <li class="contact__item">
        <svg class="contact__icon" viewBox="0 0 16 16"><path d="M1 3h14v10H1zm1.5 1.2L8 8.5l5.5-4.3z"/></svg>
        info@yourwebsitehere.com
      </li>
      <li class="contact__item">
        <svg class="contact__icon" viewBox="0 0 16 16"><circle cx="8" cy="8" r="7"/><path d="M1 8h14M8 1c-3 3-3 11 0 14M8 1c3 3 3 11 0 14" stroke="#fff" stroke-width="1" fill="none"/></svg>
        yourwebsitehere.com
      </li>
    </ul>
  </div>
</section>

</body>
</html>
```